Here's your chance to make lots of children happy! Colourful and fun bag design for candies

Happy New Year 2019 to all you creative souls out there! It's time to create a design that would bring happiness to a lot of children, big and small, all around the world! We are updating our packaging to make it more colourful, attractive/cute and fun. This assignment is for a series of 5 designs for 5 different candy flavours - Coconut HARD Candy (with Western Australian Sea Salt), Coconut CHEWY candy, Cola, Mint, and Tamarind. The general look of the 5 packaging must be similar. To differentiate, please use different colours, product name (the above 5 flavours) and pictures representing the flavours. As you can see, from our old packaging, the designs are very fragmented. The front dimension of the bag is 145mm wide and 205mm height, including sealing area: Top seal - 25mm, bottom seal 15mm. Our parent logo is SunKite and appears on the top left. You may or may not include an open window to show the wrapped candies inside, depending on your design. Please see attached files for our old designs. You may use the included draft template as a guide, you may choose to use our old pictures or new ones. A couple of our latest packaging series are also attached. Other products can be found on our website - www.velortaq.com.my. Please do not use large areas of white or black as much as possible in your design.

Target Market(s)

Target audience - children for mint and cola, adults for coconut and tamarind

Font styles to use
Sans Serif

Requirements
Should not have
• Large blocks of white or black

```html
<!DOCTYPE html>
<html lang="en">
<head>
<meta charset="UTF-8">
<title>SunKite Coconut Chewy Candy – Bag Front</title>
<link rel="stylesheet" href="https://fonts.googleapis.com/css2?family=Fredoka:wght@500;600;700&display=swap">
<style>
  :root {
    --page-bg: #f2f4f4;
    --stripe-light: #1c9d92;
    --stripe-dark: #0e7c75;
    --band-light: #1a978c;
    --band-dark: #0b6a64;
    --white: #ffffff;
    --brand-red: #d7252a;
    --coconut-green: #7cbf2a;
    --coconut-deep: #3f8f1e;
    --candy-yellow: #f6d21a;
    --candy-orange: #f0a01a;
    --outline-blue: #1b8fd6;
    --illustration-a: #8cc04a;
    --illustration-b: #3e9ad8;
    --illustration-c: #d94a1e;
  }
  * { box-sizing: border-box; margin: 0; padding: 0; }
  html, body {
    width: 1200px; height: 1200px; overflow: hidden;
    background: var(--page-bg);
    font-family: "Fredoka", sans-serif;
  }
  .bag {
    position: absolute; left: 220px; top: 52px;
    width: 760px; height: 1095px;
    background: repeating-linear-gradient(90deg,
      var(--stripe-light) 0 46px, var(--stripe-dark) 46px 92px);
    overflow: hidden;
  }
  .seal {
    position: absolute; left: 0; width: 100%;
    background: repeating-linear-gradient(180deg,
      var(--band-light) 0 6px, var(--band-dark) 6px 10px);
  }
  .seal--top { top: 0; height: 100px; }
  .seal--bottom { bottom: 0; height: 95px; }
  .brand {
    position: absolute; left: 18px; top: 145px;
    height: 50px; padding: 0 14px 0 8px;
    display: flex; align-items: center; gap: 10px;
    background: var(--brand-red);
    border: 3px solid var(--white);
  }
  .brand__mark { width: 26px; height: 26px; background: var(--white); }
  .brand__name { color: var(--white); font-weight: 700; font-size: 30px; letter-spacing: 1px; }
  .flavour {
    position: absolute; right: 40px; top: 178px;
    color: var(--white); font-weight: 600; font-size: 52px;
    line-height: 1.02; text-align: right;
  }
  .hero-art {
    position: absolute; left: 59px; top: 283px;
    width: 600px; height: 403px;
    border-radius: 40px;
    background:
      radial-gradient(circle at 50% 48%, var(--illustration-a) 0 30%, transparent 55%),
      linear-gradient(135deg, var(--illustration-b) 0%, var(--illustration-a) 55%, var(--illustration-c) 100%);
    opacity: .9;
  }
  .product {
    position: absolute; left: 0; width: 100%; text-align: center;
  }
  .product__name {
    top: 655px;
    font-weight: 700; font-size: 128px; letter-spacing: -2px;
    color: var(--coconut-green);
    -webkit-text-stroke: 5px var(--candy-yellow);
    paint-order: stroke fill;
    text-shadow: 0 7px 0 var(--coconut-deep);
  }
  .product__type {
    top: 790px; padding-left: 100px;
    font-weight: 700; font-size: 78px;
    color: var(--candy-yellow);
    -webkit-text-stroke: 8px var(--outline-blue);
    paint-order: stroke fill;
    transform: rotate(-4deg);
  }
  .product__claim {
    top: 888px; padding-left: 70px;
    font-weight: 600; font-size: 44px;
    color: var(--white);
    transform: rotate(-5deg);
  }
</style>
</head>
<body>
  <main class="bag">
    <div class="seal seal--top"></div>
    <div class="brand"><span class="brand__mark"></span><span class="brand__name">SunKite</span></div>
    <p class="flavour">Coconut<br>Milk</p>
    <div class="hero-art" role="img" aria-label="Illustration of young green coconuts surrounded by yellow, green and orange chewy candy pieces on a blue star"></div>
    <h1 class="product product__name">COCONUT</h1>
    <p class="product product__type">Chewy Candy</p>
    <p class="product product__claim">Natural &amp; Creamy</p>
    <div class="seal seal--bottom"></div>
  </main>
</body>
</html>
```